Travel Health Brief Beautiful and Simple PDF design showing risks on your travels

Please see the attached PDF named "Bluefern Journey Wellness Brief", and the document for the full brief for tis work.
This document is a summary of a traveller's planned trip itinerary and any associated health risks from diseases and the related vaccines available. It is available for purchase once the traveller has provided us with information about their trip.
Although this document contains all the required content and the correct colour scheme, its design needs to be of a quality that reflects its purchase price. It would benefit from looking more attractive and for its data to be laid out in a way to make it more easily readable.

Target Market
Individuals, families and professionals looking to plan international travel.

Deliverables
The project will deliver a new design for the PDF in vector format (preferably a layered AI file), along with individual vector files for any illustrations created for the project.

Design Overview
This document will be displayed onscreen in HTML format so the design needs to work well for both print and web.
The design must follow the attached Bluefern Journey Wellness brand book, we like the colour scheme we have and do not wish to digress too much from this.
The use of appropriate illustration and iconography is encouraged. These can add additional colours so long as these are complementary to the existing palette.
We will be looking for:
● Attractive layout
● Appropriate illustration
● Good use of whitespace
● Good choice of font size to denote information hierarchy
● Recognisably the same branding as the current sample document provided

Specific Notes on Content
The Your Trip section could contain 1 destination or many. The design must accommodate any number of destinations. It should be optimised to look best for trips of 1 to 3 destinations.
The design of the map pins cannot change.
The map is a static mapvora map and will be using the colour scheme and map pins displayed.
This map can be a maximum image size of 640 x 640 pixels, but this can be stretched in the PDF - however if it's too big it will look blurry so the size it is now is about perfect.
One idea we have had is to include infographic summary data on the first page below the map/itinerary. Perhaps counts for each disease risk category.
The colours we have chosen for each disease risk category are not set in stone, but we want to avoid any sort of traffic light (red/amber/green) colours. You are welcome to stick with the existing colours.
The number of diseases in each section is completely dynamic. There could be, none, one or many, so the design needs to accommodate that without being too linear and boring a layout, like it is at the moment.
The example we've provided purposefully includes most of the diseases in question so you can see what the content looks like for each one.
The hyperlinks could theoretically be any length. We have left them as URLs rather than link text as the PDF document needs to be printable. In the onscreen version we use link text.
Updates

Target Market(s)

Individual travellers researching the risk of foreign travel

Industry/Entity Type

Healthcare, travel

Requirements
Must have
• See brief
Nice to have
• See brief

```html
<!DOCTYPE html>
<html lang="en">
<head>
<meta charset="utf-8">
<title>Bluefern Journey Wellness Brief</title>
<link rel="stylesheet" href="https://fonts.googleapis.com/css2?family=Arimo:wght@400;700&display=swap">
<style>
  :root {
    --brand-navy: #0f2a4a;
    --brand-blue: #0e6690;
    --band-blue: #00648c;
    --pin-blue: #5ab4d9;
    --text-grey: #444a4f;
    --panel-bg: #eef6fa;
    --map-land: #eceeef;
    --map-water: #c4d4da;
    --white: #ffffff;
  }
  * { box-sizing: border-box; margin: 0; padding: 0; }
  html, body { width: 1200px; height: 1200px; overflow: hidden; background: var(--white); }
  body { font-family: "Arimo", Arial, sans-serif; color: var(--text-grey); position: relative; }

  .brand { position: absolute; left: 138px; top: 128px; display: flex; align-items: center; gap: 18px; }
  .brand-dot { width: 64px; height: 64px; border-radius: 50%; background: var(--brand-blue); }
  .brand-name { font-size: 30px; font-weight: 700; color: var(--brand-navy); line-height: 1.15; width: 220px; }

  .doc-title { position: absolute; left: 139px; top: 282px; font-size: 48px; font-weight: 400; color: var(--brand-blue); letter-spacing: -0.3px; }

  .traveller { position: absolute; left: 139px; top: 392px; font-size: 27px; }
  .report-date { position: absolute; right: 110px; top: 393px; font-size: 20px; }

  .trip { position: absolute; left: 86px; top: 479px; width: 1054px; height: 455px; display: flex; }
  .trip-summary { width: 468px; background: var(--panel-bg); padding: 54px 0 0 53px; }
  .trip-heading { font-size: 25px; font-weight: 700; color: var(--text-grey); margin-bottom: 26px; }
  .stop { display: flex; align-items: flex-start; gap: 14px; margin-bottom: 22px; }
  .stop-pin { width: 40px; height: 52px; flex: none; }
  .stop-city { font-size: 24px; color: var(--brand-blue); margin-top: 2px; }
  .stop-date { font-size: 17px; margin-top: 6px; }
  .trip-return { font-size: 20px; line-height: 1.2; margin-top: 30px; width: 380px; }

  .trip-map { flex: 1; position: relative; background: linear-gradient(100deg, var(--map-water) 0 14%, var(--map-land) 14% 82%, var(--map-water) 82%); }
  .map-credit { position: absolute; left: 8px; bottom: 6px; font-size: 17px; font-weight: 700; color: var(--white); text-shadow: 0 0 2px #777; }

  .section-title { position: absolute; left: 139px; top: 988px; font-size: 27px; font-weight: 700; color: var(--brand-blue); }
  .risk-band { position: absolute; left: 86px; top: 1052px; width: 1054px; height: 55px; background: var(--band-blue); color: var(--white); font-size: 24px; font-weight: 700; padding: 14px 0 0 53px; }
</style>
</head>
<body>
  <header class="brand">
    <span class="brand-dot"></span>
    <span class="brand-name">Bluefern Journey Wellness</span>
  </header>

  <h1 class="doc-title">Bluefern Journey Wellness Brief</h1>
  <p class="traveller">Ruth Ellery</p>
  <p class="report-date">Report produced on 20 Jul 2023, 16:26</p>

  <section class="trip">
    <div class="trip-summary">
      <h2 class="trip-heading">Your trip</h2>
      <div class="stop">
        <svg class="stop-pin" viewBox="0 0 40 52"><path d="M20 51 L6 33 A18 18 0 1 1 34 33 Z" fill="var(--pin-blue)"/><text x="20" y="27" text-anchor="middle" font-family="Arimo, Arial, sans-serif" font-size="17" font-weight="700" fill="#fff">1</text></svg>
        <div><p class="stop-city">Luanda, Angola</p><p class="stop-date">On 17 August 2023</p></div>
      </div>
      <div class="stop">
        <svg class="stop-pin" viewBox="0 0 40 52"><path d="M20 51 L6 33 A18 18 0 1 1 34 33 Z" fill="var(--pin-blue)"/><text x="20" y="27" text-anchor="middle" font-family="Arimo, Arial, sans-serif" font-size="17" font-weight="700" fill="#fff">2</text></svg>
        <div><p class="stop-city">Nairobi, Kenya</p><p class="stop-date">On 24 August 2023</p></div>
      </div>
      <p class="trip-return">Returning on 31 August 2023, a total of 15 days</p>
    </div>
    <div class="trip-map" role="img" aria-label="Map of central and east Africa with pins at Luanda and Nairobi">
      <span class="map-credit">mapvora</span>
    </div>
  </section>

  <h2 class="section-title">Disease risks and vaccines for your trip</h2>
  <div class="risk-band">Mandatory</div>
</body>
</html>
```